Finance Broker helping people meet their personal and business goals

New business card design,
1st look at the old business card so this makes sense.
I DON'T want:
the subtext "For all your Rural and Commercial Finance".
I DON'T want the: "and Management Consultant" words
I DON'T want the old phone: 07 48213957
I DON'T want the fax number: 07 45826031
I DON'T want the email address: tallowcreek@brightlink.com.au
I DON'T want the flower
What I DO want
I DO want the mobile 0451 836 209 (in larger text)
I DO want:
My name: Dennis Harwell-Lowe
I DO want: Australian Credit Licence 529164 (Tallow Creek Pty Ltd)
I DO want: Principal Finance Broker
I DO want new email: dennis@plotnextstep.com.au
I DO want address: PO Box 928, Tully Qld 4854
I DO want the existing logo (PNS on existing card)

Target Market(s)

Business Borrowers, Home Purchasers, and People wanting to finance cars and plant and equipment

Industry/Entity Type

Financial Service

Contact Information for Business Card

See project description

Font styles to use
Serif

Colors

Designer to choose colors to be used in the design.

Requirements
Must have
• See project description
Nice to have
• Black and Yellow colours
Should not have
• See project description

```html
<!DOCTYPE html>
<html lang="en">
<head>
<meta charset="utf-8">
<title>Plot Next Step – Business Card</title>
<link rel="stylesheet" href="https://fonts.googleapis.com/css2?family=Arimo:wght@400;700&family=Libre+Baskerville:wght@400;700&display=swap">
<style>
  :root {
    --page: #f4f5f7;
    --card: #2b2a29;
    --yellow: #f9f53b;
    --white: #ffffff;
    --serif: "Libre Baskerville", Georgia, serif;
    --sans: "Arimo", "Helvetica Neue", Arial, sans-serif;
  }
  * { margin: 0; padding: 0; box-sizing: border-box; }
  html, body {
    width: 1200px; height: 1000px; overflow: hidden;
    background: var(--page);
  }
  .card {
    position: absolute; left: 294px;
    width: 612px; height: 375px;
    background: var(--card);
  }
  .card--front { top: 108px; }
  .card--back { top: 517px; }
  .card > * { position: absolute; white-space: nowrap; }

  .wordmark {
    left: 44px; top: 60px;
    font-family: var(--serif); font-size: 32px; line-height: 1;
    color: var(--yellow); letter-spacing: -0.5px;
  }
  .tagline {
    left: 45px; top: 97px;
    font-family: var(--serif); font-size: 14.5px; line-height: 1;
    color: var(--white); letter-spacing: 0.6px;
  }
  .brand-mark {
    display: flex; align-items: center; gap: 10px;
  }
  .brand-mark__dot {
    display: block; border-radius: 50%; background: var(--yellow);
  }
  .brand-mark__name {
    font-family: var(--serif); font-weight: 400; color: var(--yellow); line-height: 1;
  }
  .card--front .brand-mark { right: 42px; top: 50px; }
  .card--front .brand-mark__dot { width: 72px; height: 72px; }
  .card--front .brand-mark__name { font-size: 40px; }

  .person-name {
    left: 44px; top: 174px;
    font-family: var(--sans); font-weight: 700; font-size: 25px; line-height: 1;
    color: var(--white);
  }
  .licence {
    left: 44px; top: 207px;
    font-family: var(--sans); font-size: 15px; line-height: 1;
    color: var(--white); letter-spacing: -0.3px;
  }
  .role {
    left: 44px; top: 229px;
    font-family: var(--sans); font-size: 15.5px; line-height: 1;
    color: var(--yellow);
  }
  .mobile {
    left: 44px; top: 300px;
    display: flex; align-items: center; gap: 11px;
    font-family: var(--sans); font-size: 32px; line-height: 1;
    color: var(--white); letter-spacing: -0.5px;
  }
  .contact {
    right: 42px; top: 298px; text-align: right;
    font-family: var(--sans); font-size: 15px; line-height: 19px;
    color: var(--white); letter-spacing: -0.3px;
  }

  .card--back .brand-mark {
    left: 50%; top: 140px; transform: translateX(-50%);
    gap: 16px;
  }
  .card--back .brand-mark__dot { width: 96px; height: 96px; }
  .card--back .brand-mark__name { font-size: 56px; }
  .website {
    left: 0; right: 0; top: 298px; text-align: center;
    font-family: var(--sans); font-size: 15px; line-height: 1;
    color: var(--white); letter-spacing: -0.2px;
  }
</style>
</head>
<body>
  <section class="card card--front">
    <p class="wordmark">Plot Next Step</p>
    <p class="tagline">A Member of the Tallow Creek Group</p>
    <div class="brand-mark">
      <span class="brand-mark__dot"></span>
      <span class="brand-mark__name">PNS</span>
    </div>

    <h1 class="person-name">DENNIS HARWELL-LOWE</h1>
    <p class="licence">Australian Credit Licence 529164 (Tallow Creek Pty Ltd)</p>
    <p class="role">PRINCIPAL FINANCE BROKER</p>

    <p class="mobile">
      <svg class="mobile__icon" width="19" height="28" viewBox="0 0 19 28" aria-hidden="true">
        <rect x="1.5" y="1.5" width="16" height="25" rx="3" fill="none" stroke="#f9f53b" stroke-width="3"/>
        <rect x="5" y="6" width="9" height="14" fill="#f9f53b"/>
        <circle cx="9.5" cy="23" r="1.3" fill="#f9f53b"/>
      </svg>
      <span>0451 836 209</span>
    </p>
    <p class="contact">PO Box 928, Tully Qld 4854<br>dennis@plotnextstep.com.au</p>
  </section>

  <section class="card card--back">
    <div class="brand-mark">
      <span class="brand-mark__dot"></span>
      <span class="brand-mark__name">PNS</span>
    </div>
    <p class="website">www.plotnextstep.com.au</p>
  </section>
</body>
</html>
```